Brookvine Estates Business Card

Business Card:

Somewhere on front of card, please include Broker License Number: 5839261

Website is BrookvineEstates.com

Address is:
7216 Orchardpine Ave E
Saginaw, MI 48517

I'll let you use creative freedom on the rest; we obviously need Name, Title, Email (@BrookvineEstates.com), Office Phone, Cell Phone.

Don't want any special die-cutting, just a standard size business card.

On the back, include a place for the date and time of an appointment to be written in pen.

Industry/Entity Type

Business

Requirements
Must have
• Our logo, attached to email.

```html
<!DOCTYPE html>
<html lang="en">
<head>
<meta charset="utf-8">
<title>Brookvine Estates Business Card</title>
<link rel="stylesheet" href="https://fonts.googleapis.com/css2?family=Open+Sans:wght@400;600;700&family=Tinos&display=swap">
<style>
  :root {
    --page: #ecebe8;
    --brand-blue: #2e2c8c;
    --ink: #111111;
    --card-grey-light: #e7e7e9;
    --card-grey-dark: #c4c4c8;
    --paper: #ffffff;
    --photo-light: #d9d4c8;
    --photo-dark: #8f8778;
    --watermark: rgba(46, 44, 140, 0.09);
  }
  * { box-sizing: border-box; margin: 0; padding: 0; }
  html, body { width: 1200px; height: 892px; overflow: hidden; background: var(--page); }
  body { position: relative; font-family: "Open Sans", Arial, sans-serif; color: var(--ink); }

  .card {
    position: absolute;
    left: 250px;
    width: 700px;
    height: 400px;
    overflow: hidden;
    box-shadow: 0 4px 14px rgba(0,0,0,0.18);
  }
  .card-front { top: 28px; background: linear-gradient(160deg, var(--card-grey-light), var(--card-grey-dark)); }
  .card-back { top: 460px; background: var(--paper); }

  .front-art { position: absolute; inset: 0; }

  .front-info {
    position: absolute;
    right: 26px;
    bottom: 20px;
    text-align: right;
    display: flex;
    flex-direction: column;
    align-items: flex-end;
  }
  .brand-name {
    font-weight: 700;
    font-size: 40px;
    color: var(--brand-blue);
    line-height: 1;
    margin-bottom: 10px;
    display: flex;
    align-items: center;
    gap: 10px;
  }
  .brand-mark { width: 14px; height: 14px; background: var(--brand-blue); }
  .person-name { font-family: "Tinos", "Times New Roman", serif; font-size: 30px; color: var(--brand-blue); line-height: 1.05; }
  .person-title { font-weight: 700; font-size: 17px; line-height: 1.2; }
  .license { font-size: 16px; color: var(--brand-blue); margin-bottom: 6px; }
  .contact-line { display: flex; align-items: center; gap: 10px; font-size: 15px; line-height: 21px; }
  .contact-icon { width: 15px; height: 15px; flex: none; }

  .back-rule {
    position: absolute; left: 0; top: 44px; width: 240px; height: 6px;
    border-top: 2px solid var(--ink); border-bottom: 2px solid var(--ink);
  }
  .back-heading {
    position: absolute; left: 262px; top: 30px;
    font-weight: 600; font-size: 28px; letter-spacing: 1px; color: var(--brand-blue);
  }
  .watermark {
    position: absolute; left: 0; right: 0; top: 150px; text-align: center;
    font-weight: 700; font-size: 96px; color: var(--watermark); line-height: 1;
  }
  .slot { position: absolute; top: 110px; width: 240px; }
  .slot-date { left: 120px; }
  .slot-time { left: 400px; }
  .slot-label { font-weight: 600; font-size: 28px; margin-bottom: 14px; }
  .write-line { height: 34px; border-bottom: 5px dotted var(--ink); width: 220px; }
</style>
</head>
<body>

<section class="card card-front">
  <svg class="front-art" viewBox="0 0 700 400" width="700" height="400">
    <path role="img" aria-label="Photo of a two-storey house with garage, front steps and pink flowering shrubs"
          d="M0,0 H640 C610,120 420,238 0,252 Z" fill="url(#photoTone)"/>
    <path d="M0,262 C300,252 560,190 700,96" fill="none" stroke="var(--brand-blue)" stroke-width="9"/>
    <defs>
      <linearGradient id="photoTone" x1="0" y1="0" x2="1" y2="1">
        <stop offset="0" stop-color="#b9b4ab"/>
        <stop offset="0.5" stop-color="#d9d4c8"/>
        <stop offset="1" stop-color="#8f8778"/>
      </linearGradient>
    </defs>
  </svg>

  <div class="front-info">
    <div class="brand-name"><span class="brand-mark"></span>Brookvine Estates</div>
    <div class="person-name">Daniel Hartwell</div>
    <div class="person-title">manager</div>
    <div class="license">License Number: 5839261</div>
    <div class="contact-line">+94 5612 3387
      <svg class="contact-icon" viewBox="0 0 16 16"><rect width="16" height="16" fill="#111"/><path d="M4 3h3l1 3-2 1c1 2 2 3 3 3l1-2 3 1v3c-6 0-9-3-9-9z" fill="#fff"/></svg></div>
    <div class="contact-line">+94 5648 2219
      <svg class="contact-icon" viewBox="0 0 16 16"><rect width="16" height="16" fill="#111"/><rect x="5" y="2.5" width="6" height="11" rx="1" fill="#fff"/><rect x="6" y="4" width="4" height="7" fill="#111"/></svg></div>
    <div class="contact-line">7216 Orchardpine Ave E Saginaw, MI 48517
      <svg class="contact-icon" viewBox="0 0 16 16"><rect width="16" height="16" fill="#111"/><path d="M8 2a4 4 0 0 1 4 4c0 3-4 8-4 8S4 9 4 6a4 4 0 0 1 4-4z" fill="#fff"/><circle cx="8" cy="6" r="1.5" fill="#111"/></svg></div>
    <div class="contact-line">www.BrookvineEstates.com
      <svg class="contact-icon" viewBox="0 0 16 16"><rect width="16" height="16" fill="#111"/><circle cx="8" cy="8" r="5" fill="none" stroke="#fff" stroke-width="1.3"/><path d="M3 8h10M8 3c-2 3-2 7 0 10M8 3c2 3 2 7 0 10" fill="none" stroke="#fff" stroke-width="1"/></svg></div>
    <div class="contact-line">daniel@BrookvineEstates.com
      <svg class="contact-icon" viewBox="0 0 16 16"><rect width="16" height="16" fill="#111"/><rect x="3" y="4.5" width="10" height="7" fill="#fff"/><path d="M3 4.5l5 4 5-4" fill="none" stroke="#111" stroke-width="1"/></svg></div>
  </div>
</section>

<section class="card card-back">
  <div class="back-rule"></div>
  <div class="back-heading">APPOINTMENT</div>
  <div class="watermark">Brookvine Estates</div>
  <div class="slot slot-date">
    <div class="slot-label">Date</div>
    <div class="write-line"></div>
    <div class="write-line"></div>
    <div class="write-line"></div>
    <div class="write-line"></div>
    <div class="write-line"></div>
  </div>
  <div class="slot slot-time">
    <div class="slot-label">Time</div>
    <div class="write-line"></div>
    <div class="write-line"></div>
    <div class="write-line"></div>
    <div class="write-line"></div>
    <div class="write-line"></div>
  </div>
</section>

</body>
</html>
```